German Headhunter/ HR Consultancy needs Business Cards Design

We need a business Card Design for our Company in Stuttgart. We are specialized as Headhunter/ HR Consultancy in Placement of specialist and managers in permanent employment. Please refer to our business logo.

```html
<!DOCTYPE html>
<html lang="de">
<head>
<meta charset="utf-8">
<title>Kernwerk Personalberatung – Visitenkarte</title>
<link href="https://fonts.googleapis.com/css2?family=Arimo:wght@400;700&display=swap" rel="stylesheet">
<style>
  :root {
    --brand-blue: #3a4ea6;
    --brand-blue-light: #5468b8;
    --brand-blue-dark: #2f4194;
    --ink: #1c1c1c;
    --muted: #444;
    --rule: #cfcfcf;
    --edge-grey: #5a5a5a;
    --paper: #ffffff;
    --stage: #e9eaee;
  }
  * { box-sizing: border-box; margin: 0; padding: 0; }
  html, body { width: 1200px; height: 1120px; overflow: hidden; }
  body {
    background: var(--stage);
    font-family: "Arimo", Arial, sans-serif;
    display: flex;
    flex-direction: column;
    align-items: center;
    justify-content: center;
    gap: 40px;
  }
  .card {
    position: relative;
    width: 840px;
    height: 480px;
    overflow: hidden;
    box-shadow: 0 8px 24px rgba(0,0,0,.15);
  }

  /* brand lockup */
  .brand {
    position: absolute;
    display: flex;
    align-items: center;
    gap: 16px;
    font-weight: 700;
    text-transform: uppercase;
    letter-spacing: 1px;
    line-height: 1.15;
    white-space: nowrap;
  }
  .brand-mark { width: 30px; height: 30px; flex: none; }
  .brand-name { display: flex; flex-direction: column; }

  /* front */
  .card-front { background: var(--paper); }
  .card-front .brand { left: 70px; top: 112px; color: var(--brand-blue); font-size: 26px; }
  .card-front .brand-mark { background: var(--brand-blue); }
  .person { position: absolute; right: 60px; top: 108px; text-align: right; }
  .person-name { font-size: 36px; font-weight: 700; color: var(--ink); }
  .person-role { font-size: 20px; color: var(--brand-blue); margin-top: 4px; }
  .divider {
    position: absolute;
    left: 40px; right: 40px; top: 236px;
    height: 1px; background: var(--rule);
  }
  .contacts {
    position: absolute; left: 70px; top: 290px;
    list-style: none; font-size: 19px; color: var(--muted); line-height: 30px;
  }
  .contacts li { display: flex; align-items: center; gap: 12px; }
  .contacts svg { width: 16px; height: 16px; flex: none; }
  .address {
    position: absolute; right: 60px; top: 270px;
    text-align: right; font-style: normal; font-size: 19px; color: var(--muted); line-height: 30px;
  }
  .edge-band { position: absolute; left: 0; right: 0; bottom: 0; height: 16px; display: flex; }
  .edge-band .band-blue { flex: 0 0 55%; background: var(--brand-blue); }
  .edge-band .band-grey { flex: 1; background: var(--edge-grey); }

  /* back */
  .card-back { background: var(--brand-blue); }
  .back-pattern {
    position: absolute; inset: 0;
    background: linear-gradient(160deg, var(--brand-blue-dark) 0%, var(--brand-blue) 45%, var(--brand-blue-light) 100%);
  }
  .card-back .brand {
    left: 50%; top: 50%; transform: translate(-50%, -50%);
    color: #fff; font-size: 30px;
  }
  .card-back .brand-mark { background: #fff; }
</style>
</head>
<body>

  <section class="card card-front" aria-label="Vorderseite der Visitenkarte">
    <div class="brand">
      <span class="brand-mark"></span>
      <span class="brand-name"><span>Kernwerk</span><span>Personalberatung</span></span>
    </div>

    <div class="person">
      <div class="person-name">Jonas Albrecht</div>
      <div class="person-role">Geschäftsführer</div>
    </div>

    <div class="divider"></div>

    <ul class="contacts">
      <li>
        <svg viewBox="0 0 16 16" aria-hidden="true"><circle cx="8" cy="8" r="8" fill="#3a4ea6"/><path d="M5 4.5l1.6-.4.8 2-1 .7a5 5 0 0 0 2.8 2.8l.7-1 2 .8-.4 1.6c-3.4.2-6.7-3.1-6.5-6.5z" fill="#fff"/></svg>
        +49 1520 4187265
      </li>
      <li>
        <svg viewBox="0 0 16 16" aria-hidden="true"><circle cx="8" cy="8" r="8" fill="#3a4ea6"/><rect x="4" y="5.5" width="8" height="5.5" fill="#fff"/><path d="M4 5.5l4 3 4-3" stroke="#3a4ea6" fill="none" stroke-width="1"/></svg>
        kontakt@kernwerk-personal.de
      </li>
      <li>
        <svg viewBox="0 0 16 16" aria-hidden="true"><circle cx="8" cy="8" r="8" fill="#3a4ea6"/><circle cx="8" cy="8" r="4.5" fill="none" stroke="#fff" stroke-width="1"/><ellipse cx="8" cy="8" rx="2" ry="4.5" fill="none" stroke="#fff" stroke-width="1"/><path d="M3.5 8h9" stroke="#fff" stroke-width="1"/></svg>
        www.kernwerk-personal.de
      </li>
    </ul>

    <address class="address">Lindenweg 12, 70174<br>Stuttgart, Germany</address>

    <div class="edge-band"><span class="band-blue"></span><span class="band-grey"></span></div>
  </section>

  <section class="card card-back" aria-label="Rückseite der Visitenkarte">
    <div class="back-pattern" role="img" aria-label="Dezentes Wiederholungsmuster des Firmenzeichens auf blauem Grund"></div>
    <div class="brand">
      <span class="brand-mark"></span>
      <span class="brand-name"><span>Kernwerk</span><span>Personalberatung</span></span>
    </div>
  </section>

</body>
</html>
```